Water filter company needs packaging designs

Fendaro is a new company that makes eco-friendly water filter for consumers . we currently need designs for our 13 stage water filter, alkaline filter and their respective replacement cartridges.we would like to see a final design that reflect Eco-friendliness, safeness, uniqueness, healthiness,cleanliness and life.

* Images and Content items are attached to this brief (521985 Content 1, and 521985 Content 2).
* 3 x High Resolution Images are available at:
https://www.filevessel.example/s/8k2mq7trw4xhnpa/image%201.png
https://www.filevessel.example/s/3n71r8vze9kcd2q/image%204%20%281%29.png
https://www.filevessel.example/s/9wtkb4mhaxnqzle/image%206%20png.png"

some of the images i attached for use are also available a this filevessel link

https://www.filevessel.example/sh/qlemtv4odkarwep/KTvnPqX_R2?n=58203947
Updates

sorry everyone i forgot to add the dimensions.
13 stage and alkaline filter have the same dimensions of

Size { W x H x L }: 4.5 x 12 x 5.375 INCHES
their cartidges have the same dimensions of
Size { W x H x L }: 3.125 x 10 x 3.125 INCHES

include "Made in U.S.A" on all packaging boxes.

I just found out that the people at artmingle screwed up the order of the files I sent in for upload.Here is an update on that . For 13 stage water filter and it's replacement cartridge box, use the files with following names only  and any corresponding description - 13 stage cartridge, image 1, image 4,image 2, image 6 ,logo,front panel image,13 stage water filter and 13 stage water filter replacement cartridge.For alkaline filter and it;s replacement filter, use files with the following names only and any corresponding description-  8 stage cartridge,active girl,front panel image,glass girl, jumping girl,yoga girl,fendaro alkaline water filter, fendaro alkaline water filter replacement cartridge,logo

uploaded water splash image for background.You can revise your work with that if you wish to.Thanks

Target Market(s)

consumers for home use

Industry/Entity Type

It Company

Requirements
Must have
• must use all photos attached with appropriate descriptions
must be in retail packaging

```html
<!DOCTYPE html>
<html lang="en">
<head>
<meta charset="utf-8">
<title>Fendaro Alkaline Water Filter – Box Panels</title>
<link rel="stylesheet" href="https://fonts.googleapis.com/css2?family=Roboto+Condensed:ital,wght@0,400;0,700;1,400;1,700&display=swap">
<style>
  :root{
    --page:#e4e5e7;
    --teal-top:#2f9fb2;
    --teal-mid:#2584a3;
    --deep-blue:#1b4f86;
    --stage-box:rgba(22,60,130,.78);
    --stage-border:rgba(140,200,230,.55);
    --ink:#ffffff;
    --ink-soft:rgba(255,255,255,.86);
    --splash-light:#3aa6bd;
    --splash-dark:#16557e;
    --badge:#eef3f6;
  }
  *{box-sizing:border-box;margin:0;padding:0}
  html,body{width:1200px;height:845px;overflow:hidden}
  body{
    background:var(--page);
    font-family:"Roboto Condensed", "Arial Narrow", sans-serif;
    color:var(--ink);
    display:flex;align-items:center;justify-content:center;
  }
  .box-sides{display:flex;height:805px;box-shadow:0 10px 30px rgba(0,0,0,.18)}
  .side-panel{
    width:390px;height:100%;
    padding:22px 20px 18px;
    text-align:center;
    position:relative;overflow:hidden;
    display:flex;flex-direction:column;
  }
  .side-panel--stages{
    background:linear-gradient(180deg,var(--teal-top) 0%,var(--teal-mid) 40%,var(--deep-blue) 100%);
  }
  .side-panel--info{
    background:linear-gradient(180deg,var(--teal-mid) 0%,var(--teal-top) 35%,var(--teal-mid) 70%,var(--deep-blue) 100%);
    border-left:1px solid rgba(0,0,0,.12);
  }
  .intro{font-size:12.5px;line-height:1.35;margin-bottom:12px}
  .contaminants{font-size:10.5px;font-style:italic;line-height:1.3;color:var(--ink-soft);margin-bottom:14px}
  .stage-list{
    background:var(--stage-box);
    border:1px solid var(--stage-border);
    border-radius:14px;
    padding:14px 14px 12px;
    flex:1;
    display:flex;flex-direction:column;justify-content:space-between;
    position:relative;z-index:1;
  }
  .stage h3{font-size:12.5px;font-weight:700;margin-bottom:3px;letter-spacing:.3px}
  .stage p{font-size:12px;line-height:1.3}
  .splash{
    position:absolute;left:0;right:0;bottom:0;height:230px;
    background:radial-gradient(ellipse at 40% 70%,var(--splash-light) 0%,rgba(22,85,126,.6) 55%,transparent 80%);
    opacity:.6;
  }
  .product-title{font-size:14px;font-weight:700;font-style:italic;margin-bottom:2px}
  .product-tagline{font-size:12.5px;line-height:1.3;margin-bottom:16px}
  .info-copy{font-size:11.5px;line-height:1.33;margin-bottom:10px}
  .closing{font-size:13px;line-height:1.35;margin:10px 0 18px}
  .eco-badge{display:block;margin:0 auto 22px}
  .warranty{font-size:12.5px;font-weight:700;line-height:1.3}
  .warranty strong{display:block;font-size:13.5px;letter-spacing:.4px}
  .usage{font-size:12.5px;line-height:1.35;margin:18px 0 16px}
  .fine-print{font-size:9px;font-style:italic;line-height:1.3;color:var(--ink-soft);margin-bottom:14px}
  .side-panel--info .splash{height:260px}
  .side-panel--info > *:not(.splash){position:relative;z-index:1}
</style>
</head>
<body>
  <main class="box-sides">
    <section class="side-panel side-panel--stages">
      <div class="splash" role="img" aria-label="Blue water splash background"></div>
      <p class="intro">The truly unique and advanced Mineralized Fendaro Alkaline Water Filter removes dozens of harmful particles and other contaminants* below the U.S. EPA recommended content levels. The Mineralized Fendaro Alkaline Water Filter provides 13 unique filtration stages that prevent these particles from proceeding into your water. At the same time, this advanced filtration system remineralizes your clean water with calcium, potassium and other vital minerals that your body needs!</p>
      <p class="contaminants">*Contaminants include: Chlorine, cysts, heavy metals, herbicides, VOCs, asbestos, Giardia, arsenic, bromide, PBCs, bacteria, protozoa, radiation particles, medication residue, hydrogen sulfide, pesticides, trihalomethanes, cadmium, petrochemicals, sediment and many others.</p>
      <div class="stage-list">
        <div class="stage"><h3>STAGE 1</h3><p>A layer of granular active carbon (G.A.C), which reduces carcinogenic particles and other harmful organic contaminants.</p></div>
        <div class="stage"><h3>STAGE 2</h3><p>A primary 5-micron filter pad filters tiny particles from water, such as minute solids and sediment.</p></div>
        <div class="stage"><h3>STAGE 3</h3><p>Alkaline beads, which increase pH level leaving essential minerals like magnesium, potassium, calcium etc in your water.</p></div>
        <div class="stage"><h3>STAGE 4</h3><p>A second 5-micron filter pad, removes additional small particles and sediment.</p></div>
        <div class="stage"><h3>STAGE 5</h3><p>Zeolite layer, which is a natural porous rock, eliminates strong odors and poor taste in water.</p></div>
        <div class="stage"><h3>STAGE 6</h3><p>A third 5-micron filter pad, removes additional small particles and sediment.</p></div>
        <div class="stage"><h3>STAGE 7</h3><p>Calcite, which increases water pH and reduces its acidic thereby, renders a favorable recommended level of alkalinity.</p></div>
        <div class="stage"><h3>STAGE 8</h3><p>0.5 micron carbon block eliminates organic contaminants, like pesticides, herbicides, arsenic, lead, mercury and carcinogens such as trihalomethane.</p></div>
      </div>
    </section>

    <section class="side-panel side-panel--info">
      <div class="splash" role="img" aria-label="Blue water splash background"></div>
      <h2 class="product-title">Mineralized Fendaro Alkaline Water Filter</h2>
      <p class="product-tagline">For the purest water that hydrates and provides vital minerals!</p>
      <p class="info-copy">Developed by a leading microbiologist, the patent pending Mineralized Fendaro Alkaline Water Filter offers 8 distinct filtration stages that reduce and eliminate some of the most harmful particles, while adding vital minerals to your delicious pure water!</p>
      <p class="info-copy">The Mineralized Fendaro Alkaline Water Filter is also eco-friendly, created from natural filter materials. It's free of all BPA particles and is also biodegradable!</p>
      <p class="info-copy">The Mineralized Fendaro Alkaline Water Filter has been independently tested by a leading laboratory to insure the highest quality of construction and effective function.</p>
      <p class="info-copy">The Mineralized Fendaro Alkaline Water Filter creates a remarkable pH level of only 8.3, which is ideal for most users.</p>
      <p class="info-copy">This heavy-duty filter provides over 1500 gallons of pure, delicious, alkaline water!</p>
      <p class="closing">For the very best water, enjoy the advanced Mineralized Fendaro Alkaline Water Filter today!</p>
      <svg class="eco-badge" width="84" height="84" viewBox="0 0 84 84" role="img" aria-label="Certification badge">
        <circle cx="42" cy="42" r="38" fill="var(--badge)"/>
      </svg>
      <p class="warranty">We offer all of our valued customers with a complete <strong>ONE-YEAR WARRANTY</strong></p>
      <p class="usage">Mineralized Fendaro Alkaline Water Filters may be used with a standard water tap quickly and easily.</p>
      <p class="fine-print">Note: Depending upon usage, the Mineralized Fendaro Alkaline Water Filter will operate and provide alkaline water for one year or approximately 1500 gallons or a total of use.</p>
      <p class="fine-print">Warning: Use the Mineralized Fendaro Alkaline Water Filter with municipal water sources only.</p>
    </section>
  </main>
</body>
</html>
```